online jewellery store business card

all black business card, glossy, with gold writing, gold logo and name (provided). simple design.

Target Market(s)

This business card is to put with purchases, so it just needs the logo and name Solvane Jewellery which I have uploaded pictures for you to use. Then it needs the web address, markolo address, email address and then the like us on CH for 10% off. All words to be used have been provided. Thanks

Industry/Entity Type

Store

Contact Information for Business Card

www.solvanejewellery.com
stores.markolo.com.au/Solvane-Jewellery
info@solvanejewellery.com

Like us on chatterly for 10% off your next purchase!

Requirements
Must have
• black background
gold writing
glossy look
Should not have
• yellow writing

```html
<!DOCTYPE html>
<html lang="en">
<head>
<meta charset="utf-8">
<title>Solvane Jewellery – Thank You Card</title>
<link rel="stylesheet" href="https://fonts.googleapis.com/css2?family=Josefin+Sans:wght@300;400&family=Open+Sans:wght@400;600;700;800&display=swap">
<style>
  :root {
    --backdrop: #ececec;
    --card-black: #050505;
    --panel-black: #000000;
    --gold: #c9a55a;
    --gold-light: #f1d98e;
    --gold-deep: #8a6424;
    --rule-gold: #a8843f;
    --text-white: #ffffff;
    --text-black: #0a0a0a;
  }
  * { box-sizing: border-box; margin: 0; padding: 0; }
  html, body {
    width: 1200px;
    height: 709px;
    overflow: hidden;
    background: var(--backdrop);
  }
  .canvas {
    position: relative;
    width: 1200px;
    height: 709px;
  }
  .card {
    position: absolute;
    left: 414px;
    top: 40px;
    width: 372px;
    height: 628px;
    background: var(--card-black);
    overflow: hidden;
    box-shadow: 0 6px 18px rgba(0,0,0,0.25);
  }
  .card__gloss {
    position: absolute;
    inset: 0;
    background: linear-gradient(125deg, rgba(255,255,255,0.07) 0%, rgba(255,255,255,0.02) 35%, rgba(255,255,255,0) 36%);
    pointer-events: none;
  }
  .brand-panel {
    position: absolute;
    left: 30px;
    top: 14px;
    width: 310px;
    height: 98px;
    background: var(--panel-black);
    display: flex;
    align-items: center;
    padding-left: 12px;
  }
  .brand-panel__mark {
    width: 74px;
    height: 74px;
    border: 2px solid var(--gold);
    border-radius: 50%;
    flex: none;
  }
  .brand-panel__name {
    margin-left: 22px;
    font-family: "Josefin Sans", sans-serif;
    font-weight: 300;
    font-size: 25px;
    line-height: 32px;
    letter-spacing: 5px;
    color: var(--gold);
    text-transform: uppercase;
  }
  .divider {
    position: absolute;
    left: 0;
    width: 100%;
    display: flex;
    justify-content: center;
    align-items: center;
  }
  .divider__rule {
    width: 54px;
    height: 1px;
    background: var(--rule-gold);
  }
  .divider__badge {
    width: 16px;
    height: 16px;
    border-radius: 50%;
    background: var(--rule-gold);
    color: var(--text-black);
    font-family: "Open Sans", sans-serif;
    font-weight: 700;
    font-size: 9px;
    line-height: 16px;
    text-align: center;
  }
  .divider--web { top: 155px; }
  .divider--mail { top: 231px; }
  .contact {
    position: absolute;
    left: 0;
    width: 100%;
    text-align: center;
    font-family: "Open Sans", sans-serif;
    font-weight: 400;
    font-size: 15px;
    line-height: 21px;
    color: var(--gold);
  }
  .contact--web { top: 170px; }
  .contact--mail { top: 253px; }
  .offer-seal {
    position: absolute;
    left: 38px;
    top: 304px;
    width: 296px;
    height: 296px;
  }
  .offer-seal svg { position: absolute; inset: 0; }
  .offer-seal__text {
    position: absolute;
    inset: 0;
    display: flex;
    flex-direction: column;
    align-items: center;
    justify-content: center;
    font-family: "Open Sans", sans-serif;
    text-transform: uppercase;
    text-align: center;
  }
  .offer-seal__thanks {
    font-weight: 800;
    font-size: 19px;
    line-height: 22px;
    color: var(--text-black);
  }
  .offer-seal__purchase {
    font-weight: 600;
    font-size: 12px;
    line-height: 16px;
    color: var(--text-black);
    margin-bottom: 16px;
  }
  .offer-seal__like {
    font-weight: 700;
    font-size: 15px;
    line-height: 20px;
    color: var(--text-white);
  }
  .offer-seal__discount {
    font-weight: 800;
    font-size: 21px;
    line-height: 25px;
    color: var(--text-white);
    letter-spacing: -0.5px;
  }
  .offer-seal__next {
    font-weight: 700;
    font-size: 13px;
    line-height: 20px;
    color: var(--text-white);
  }
</style>
</head>
<body>
<main class="canvas">
  <section class="card">
    <header class="brand-panel">
      <span class="brand-panel__mark"></span>
      <h1 class="brand-panel__name">Solvane<br>Jewellery</h1>
    </header>

    <div class="divider divider--web">
      <span class="divider__rule"></span><span class="divider__badge">w</span><span class="divider__rule"></span>
    </div>
    <p class="contact contact--web">www.solvanejewellery.com<br>stores.markolo.com.au/Solvane-Jewellery</p>

    <div class="divider divider--mail">
      <span class="divider__rule"></span><span class="divider__badge">e</span><span class="divider__rule"></span>
    </div>
    <p class="contact contact--mail">info@solvanejewellery.com</p>

    <div class="offer-seal">
      <svg viewBox="0 0 296 296" width="296" height="296">
        <defs>
          <radialGradient id="ring-tone" cx="50%" cy="50%" r="50%">
            <stop offset="74%" stop-color="#2a2418"/>
            <stop offset="88%" stop-color="#5e5130"/>
            <stop offset="100%" stop-color="#2a2418"/>
          </radialGradient>
          <linearGradient id="disc-gold" x1="0" y1="0" x2="0" y2="1">
            <stop offset="0%" stop-color="#f6e39f"/>
            <stop offset="40%" stop-color="#d4b062"/>
            <stop offset="75%" stop-color="#a67a30"/>
            <stop offset="100%" stop-color="#7a5520"/>
          </linearGradient>
        </defs>
        <g role="img" aria-label="Decorative gold looped ring ornament around the seal">
          <circle cx="148" cy="148" r="147" fill="url(#ring-tone)"/>
        </g>
        <circle cx="148" cy="148" r="110" fill="url(#disc-gold)"/>
      </svg>
      <div class="offer-seal__text">
        <p class="offer-seal__thanks">Thank You</p>
        <p class="offer-seal__purchase">For Your Purchase</p>
        <p class="offer-seal__like">Like us on chatterly</p>
        <p class="offer-seal__discount">Get 10% off on</p>
        <p class="offer-seal__next">Next purchase!</p>
      </div>
    </div>

    <div class="card__gloss"></div>
  </section>
</main>
</body>
</html>
```